Global Aviation Services website

we are a start up airline/aviation services company that will operate in Australia, USA and New Zealand initially. Fundamentally the service is to airlines who fly into and out of a market yet do not wish to have their own admin, sales and marketing infrastructures. They would use us.
The company name is Tovelle.
It needs to look sophisticated, sharp and professional. We would like it designed and built in the CMS - wordpress so we can update after the project is finished when necessary. An example of who we are and a good website we like can be found at: http://brenmorcrest.com/. There is no ecommerce or interactivity other than a contact us. We do like animation for promotion. There will be links to our airline clients and sub sites or pages will exist for the various offices we have globally. Currently 6. Each of these offices will have a dedicated local URL. Please submit your suggestion of a home page and 2 internal pages. Thank you and kind regards Ingrid
Target Market(s)
airlines, airline technology companies,
Industry/Entity Type
Aviation
Coding
Coded - Design and coding required
Number of Pages Required
5+ page
Font styles to use
Look and feel

```html
<!DOCTYPE html>
<html lang="en">
<head>
<meta charset="utf-8">
<title>Tovelle — Airline/Aviation Services</title>
<link href="https://fonts.googleapis.com/css2?family=Open+Sans:wght@400;600;700&family=Titillium+Web:wght@400;600&display=swap" rel="stylesheet">
<style>
  :root {
    --navy: #16345f;
    --navy-deep: #0f2748;
    --footer-blue: #0a4fa3;
    --accent-bar: #1a56a8;
    --purple: #5a3c96;
    --purple-dark: #452c7c;
    --text-dark: #2b2b2b;
    --text-body: #7a7a7a;
    --panel-grey: #e9edf2;
    --white: #ffffff;
    --red: #e0293a;
    --green: #27b04a;
    --yellow: #d7c319;
    --date-blue: #1a56a8;
  }
  * { margin: 0; padding: 0; box-sizing: border-box; }
  html, body { width: 1200px; height: 2707px; overflow: hidden; }
  body { position: relative; font-family: "Open Sans", Arial, sans-serif; background: var(--white); color: var(--text-dark); }

  /* Hero */
  .hero { position: absolute; left: 0; top: 0; width: 1200px; height: 578px;
    background: linear-gradient(180deg, #3f5a78 0%, #6d6a5c 30%, #c2893a 55%, #b7782f 72%, #3a3026 88%, #1e1a17 100%); }
  .hero-glow { position: absolute; inset: 0; background: radial-gradient(ellipse 60% 40% at 35% 55%, rgba(255,196,96,.55), transparent 70%),
    linear-gradient(90deg, transparent 55%, rgba(40,80,120,.55) 100%); }
  .brand { position: absolute; left: 112px; top: 26px; display: flex; align-items: center; gap: 10px;
    font-family: "Titillium Web", sans-serif; font-weight: 600; font-size: 34px; color: var(--white); letter-spacing: 1px; }
  .brand-dot { width: 14px; height: 14px; border-radius: 50%; background: var(--white); }
  .menu { position: absolute; right: 112px; top: 40px; display: flex; align-items: center; gap: 8px;
    font-size: 10px; color: var(--white); letter-spacing: .5px; }
  .menu-lines { width: 13px; height: 10px; border-top: 2px solid #fff; border-bottom: 2px solid #fff; position: relative; }
  .menu-lines::after { content: ""; position: absolute; left: 0; right: 0; top: 2px; height: 2px; background: #fff; }
  .hero-rule { position: absolute; left: 112px; top: 88px; width: 976px; height: 1px; background: rgba(255,255,255,.7); }
  .hero-title { position: absolute; left: 114px; top: 312px; font-family: "Titillium Web", sans-serif; font-weight: 400;
    font-size: 50px; color: var(--white); letter-spacing: 1px; line-height: 1; text-shadow: 0 2px 6px rgba(0,0,0,.35); }
  .hero-sub { position: absolute; left: 114px; top: 374px; font-family: "Open Sans", sans-serif; font-weight: 600;
    font-size: 25px; color: var(--white); text-shadow: 0 2px 6px rgba(0,0,0,.35); }
  .dots { position: absolute; left: 563px; top: 539px; display: flex; gap: 7px; }
  .dots span { width: 11px; height: 11px; border-radius: 50%; border: 1.5px solid rgba(255,255,255,.8); background: rgba(255,255,255,.25); }
  .dots span.active { background: var(--purple); border-color: #ddd; }

  /* Feature rows */
  .feature { position: absolute; left: 0; width: 1200px; height: 356px; overflow: hidden; }
  .feature.light { background: var(--white); }
  .feature.grey { background: var(--panel-grey); }
  .photo { position: absolute; top: 0; height: 100%; }
  .photo.left { left: 0; width: 574px; clip-path: polygon(0 0, 574px 0, 496px 100%, 0 100%); }
  .photo.right { right: 0; width: 572px; clip-path: polygon(0 0, 100% 0, 100% 100%, 76px 100%); }
  .photo.sunset { background: linear-gradient(180deg, #f0a93a 0%, #e98b1c 45%, #8a3d12 72%, #2a1d17 100%); }
  .photo.network { background: radial-gradient(ellipse at 40% 40%, #1c6f78 0%, #0e3a44 50%, #0a1c22 100%); }
  .photo.dusk { background: linear-gradient(180deg, #201d2e 0%, #5a3a3c 35%, #c46b2c 62%, #6b3a24 85%, #231a1c 100%); }
  .copy { position: absolute; width: 487px; }
  .heading { position: relative; padding-left: 20px; font-family: "Titillium Web", sans-serif; font-weight: 400;
    font-size: 27px; color: var(--text-dark); line-height: 54px; height: 54px; }
  .heading::before { content: ""; position: absolute; left: 0; top: 0; width: 6px; height: 54px; background: var(--accent-bar); }
  .copy p { margin-top: 28px; font-size: 12.5px; line-height: 31.5px; color: var(--text-body); text-align: justify; }
  .more { display: flex; width: 52px; height: 48px; margin-top: 30px; background: linear-gradient(180deg, var(--purple), var(--purple-dark));
    border-radius: 2px; align-items: center; justify-content: center; }

  /* News */
  .news { position: absolute; left: 0; top: 1644px; width: 1200px; height: 473px;
    background: linear-gradient(180deg, #6f89ad 0%, #aebfd4 35%, #e7e3d8 60%, #d6b98a 85%, #b89866 100%); }
  .news-card { position: absolute; left: 112px; top: 0; width: 384px; height: 473px; background: var(--white); }
  .news-card .heading { position: absolute; left: 38px; top: 40px; }
  .news-thumb { position: absolute; left: 38px; top: 128px; width: 303px; height: 168px;
    background: linear-gradient(180deg, #e8eef5 0%, #a9bcd6 45%, #2d5ea8 100%); }
  .news-date { position: absolute; left: 38px; top: 315px; font-size: 12px; font-weight: 700; color: var(--date-blue); }
  .news-text { position: absolute; left: 38px; top: 347px; width: 303px; font-size: 12.5px; line-height: 30px; color: var(--text-body); text-align: justify; }
  .pager { position: absolute; top: 428px; width: 45px; height: 45px; background: var(--purple); display: flex; align-items: center; justify-content: center; }

  /* Contact */
  .contact { position: absolute; left: 0; top: 2117px; width: 1200px; height: 504px;
    background: linear-gradient(180deg, var(--navy) 0%, var(--navy-deep) 100%); color: var(--white); }
  .contact .heading { position: absolute; left: 112px; top: 62px; color: var(--white); font-size: 27px; }
  .send-title { position: absolute; left: 112px; top: 141px; font-family: "Titillium Web", sans-serif; font-size: 21px; }
  .field { position: absolute; border: 1.5px solid rgba(255,255,255,.8); font-size: 11.5px; padding: 17px 20px; color: var(--white); }
  .btn-send { position: absolute; left: 112px; top: 394px; width: 110px; height: 50px; background: linear-gradient(180deg, var(--purple), var(--purple-dark));
    display: flex; align-items: center; justify-content: center; gap: 7px; font-size: 14px; font-weight: 600; }
  .world { position: absolute; left: 587px; top: 67px; width: 505px; height: 325px;
    background: radial-gradient(ellipse at 50% 50%, rgba(70,110,170,.35), rgba(22,52,95,0) 70%); border-radius: 4px; }
  .pin { position: absolute; width: 16px; height: 16px; border-radius: 50%; border: 2px solid; background: rgba(0,0,0,.2); }
  .pin::after { content: ""; position: absolute; left: 3px; top: 3px; width: 6px; height: 6px; border-radius: 50%; background: currentColor; }
  .call { position: absolute; left: 776px; top: 258px; width: 208px; height: 51px; background: var(--red); border-radius: 2px;
    display: flex; align-items: center; padding-left: 16px; gap: 14px; font-size: 11.5px; white-space: nowrap; }
  .call::after { content: ""; position: absolute; right: 20px; bottom: -8px; border: 8px solid transparent; border-top-color: var(--red); border-bottom: 0; }
  .call-icon { width: 24px; height: 24px; border: 1.5px solid #fff; border-radius: 50%; display: flex; align-items: center; justify-content: center; flex: none; }
  .legend { position: absolute; left: 617px; top: 411px; display: flex; gap: 22px; font-size: 15px; }
  .legend span { display: flex; align-items: center; gap: 7px; }
  .legend i { width: 13px; height: 13px; border-radius: 50%; border: 2px solid; display: inline-block; }

  /* Footer */
  .footer { position: absolute; left: 0; top: 2621px; width: 1200px; height: 86px; background: var(--footer-blue); color: var(--white); }
  .footer small { position: absolute; left: 112px; top: 34px; font-size: 11.5px; }
  .social { position: absolute; right: 112px; top: 31px; display: flex; gap: 14px; }
  .social span { width: 18px; height: 18px; border-radius: 50%; background: rgba(255,255,255,.92); }
</style>
</head>
<body>

<header class="hero">
  <div class="hero-glow" role="img" aria-label="Airliner climbing over a city skyline at sunset"></div>
  <div class="brand"><span class="brand-dot"></span>Tovelle</div>
  <div class="menu">MENU <span class="menu-lines"></span></div>
  <div class="hero-rule"></div>
  <h1 class="hero-title">TOVELLE</h1>
  <div class="hero-sub">AIRLINE/AVIATION SERVICES</div>
  <div class="dots"><span></span><span></span><span class="active"></span><span></span></div>
</header>

<section class="feature light" style="top:578px">
  <div class="photo left sunset" role="img" aria-label="Airliner landing on a runway at sunset"></div>
  <div class="copy" style="left:601px; top:50px">
    <h2 class="heading">WHO WE ARE</h2>
    <p>Lorem ipsum dolor sit amet, consectetur adipiscing elit. Ut ultricies orci eget ipsum pretium cursus. Cras facilisis euismod ligula, id tincidunt diam ultricies ac. Praesent tristique condimentum leo, et dictum diam imperdiet in. Proin porta nibh ac ex rutrum, id aliquam elit maximus. Quisque pellentesque lectus nulla.</p>
    <a class="more" aria-label="More"><svg width="14" height="16" viewBox="0 0 14 16"><path d="M4 2l6 6-6 6" fill="none" stroke="#fff" stroke-width="3"/></svg></a>
  </div>
</section>

<section class="feature grey" style="top:933px">
  <div class="copy" style="left:112px; top:51px">
    <h2 class="heading">WHAT WE DO</h2>
    <p>Proin malesuada enim sed sem finibus, et semper enim rhoncus. Pellentesque efficitur augue ut fringilla luctus. Integer porta consectetur massa eleifend porttitor. Proin sodales, eros facilisis convallis maximus, eros diam tristique nunc, mollis posuere risus magna molestie dolor. Sed posuere facilisis justo nec aliquam.</p>
    <a class="more" aria-label="More"><svg width="14" height="16" viewBox="0 0 14 16"><path d="M4 2l6 6-6 6" fill="none" stroke="#fff" stroke-width="3"/></svg></a>
  </div>
  <div class="photo right network" role="img" aria-label="Businessman touching a glowing global flight route network"></div>
</section>

<section class="feature light" style="top:1289px">
  <div class="photo left dusk" role="img" aria-label="Airliner flying through a dusk sky"></div>
  <div class="copy" style="left:601px; top:50px">
    <h2 class="heading">OUR CLIENTS</h2>
    <p>Lorem ipsum dolor sit amet, consectetur adipiscing elit. Ut ultricies orci eget ipsum pretium cursus. Cras facilisis euismod ligula, id tincidunt diam ultricies ac. Praesent tristique condimentum leo, et dictum diam imperdiet in. Proin porta nibh ac ex rutrum, id aliquam elit maximus. Quisque pellentesque lectus nulla.</p>
    <a class="more" aria-label="More"><svg width="14" height="16" viewBox="0 0 14 16"><path d="M4 2l6 6-6 6" fill="none" stroke="#fff" stroke-width="3"/></svg></a>
  </div>
</section>

<section class="news" role="img" aria-label="View of an aircraft wing above the clouds">
  <div class="news-card">
    <h2 class="heading">LATEST NEWS</h2>
    <div class="news-thumb" role="img" aria-label="Aircraft cabin with rows of blue seats"></div>
    <div class="news-date">JAN 30, 2016</div>
    <p class="news-text">Proin sodales, eros facilisis convallis maximus, eros diam tristique nunc, mollis posuere risus</p>
    <a class="pager" style="left:0" aria-label="Previous"><svg width="10" height="12" viewBox="0 0 10 12"><path d="M7 1L2 6l5 5" fill="none" stroke="#fff" stroke-width="2"/></svg></a>
    <a class="pager" style="right:0" aria-label="Next"><svg width="10" height="12" viewBox="0 0 10 12"><path d="M3 1l5 5-5 5" fill="none" stroke="#fff" stroke-width="2"/></svg></a>
  </div>
</section>

<section class="contact">
  <h2 class="heading">CONTACT US</h2>
  <div class="send-title">SEND MAIL</div>
  <div class="field" style="left:112px; top:193px; width:204px; height:51px">Name</div>
  <div class="field" style="left:334px; top:193px; width:204px; height:51px">Email Address</div>
  <div class="field" style="left:112px; top:269px; width:426px; height:105px">Message</div>
  <div class="btn-send"><svg width="15" height="14" viewBox="0 0 15 14"><path d="M0 6L15 0 11 14 7 9z" fill="#fff"/></svg>SEND</div>

  <div class="world" role="img" aria-label="Dotted world map showing office locations"></div>
  <span class="pin" style="left:640px; top:157px; color:var(--green); border-color:var(--green)"></span>
  <span class="pin" style="left:1000px; top:290px; color:var(--red); border-color:var(--red)"></span>
  <span class="pin" style="left:1074px; top:329px; color:var(--yellow); border-color:var(--yellow)"></span>
  <div class="call"><span class="call-icon"><svg width="11" height="11" viewBox="0 0 24 24"><path d="M6.6 10.8a15 15 0 006.6 6.6l2.2-2.2c.3-.3.7-.4 1-.2 1.1.4 2.3.6 3.6.6.6 0 1 .4 1 1V20c0 .6-.4 1-1 1A17 17 0 013 4c0-.6.4-1 1-1h3.5c.6 0 1 .4 1 1 0 1.3.2 2.5.6 3.6.1.3 0 .7-.2 1z" fill="#fff"/></svg></span>CALL US : 400 718 265 30</div>
  <div class="legend">
    <span><i style="border-color:var(--red); background:rgba(224,41,58,.4)"></i>Australia</span>
    <span><i style="border-color:var(--green); background:rgba(39,176,74,.4)"></i>USA</span>
    <span><i style="border-color:var(--yellow); background:rgba(215,195,25,.4)"></i>New Zealand</span>
  </div>
</section>

<footer class="footer">
  <small>Copyright@2016 Tovelle.&nbsp; All Right Reserved.</small>
  <div class="social"><span></span><span></span><span></span><span></span></div>
</footer>

</body>
</html>
```